SOC audit and security advisory company

We are a small public accounting firm that specializes in SOC attestations for small to medium sized business throughout the U.S. Our business is much like consulting, but we form an opinion about their operational controls. We are looking for "relevance and with a hint of polished sophistication". Our logo colors are dark gray and red. Our existing site is www.veltrocheck.com for detailed information. We would like to include some type of captcha if possible. This is an information only site.

Target Market(s)

Small to medium sized financial and IT audit companies that are innovative and flexible.

Industry/Entity Type

Auditing

Coding

Coded - Design and coding required

Number of Pages Required

4 page

Font styles to use
Sans Serif

Requirements
Must have
• Good flow and attention to the content.
Nice to have
• CAPTCHA for contact us page
Should not have
• Big Bold lines.
• Too many distractions.

```html
<!DOCTYPE html>
<html lang="en">
<head>
<meta charset="utf-8">
<title>Veltro – Audit and Advisory Services</title>
<link href="https://fonts.googleapis.com/css2?family=Bebas+Neue&family=Open+Sans:wght@400;600;700&family=Roboto+Condensed:wght@400;700&display=swap" rel="stylesheet">
<style>
  :root {
    --green: #6aac44;
    --green-dark: #5a9a35;
    --orange: #f05a28;
    --amber: #f29a1e;
    --ink: #444a50;
    --text: #555;
    --white: #fff;
    --hero-a: #f3f7fa;
    --hero-b: #dfe7ec;
  }
  * { margin: 0; padding: 0; box-sizing: border-box; }
  html, body { width: 830px; height: 1200px; overflow: hidden; }
  body { position: relative; background: var(--white); font-family: "Open Sans", sans-serif; color: var(--text); }
  h1, h2, h3 { font-weight: 400; }
  .abs { position: absolute; }

  .hero {
    left: 0; top: 0; width: 830px; height: 466px;
    background: linear-gradient(160deg, var(--hero-a) 0%, #e9eff3 45%, var(--hero-b) 100%);
  }
  .brand { left: 56px; top: 26px; font-family: "Roboto Condensed", sans-serif; font-size: 40px; font-weight: 400; color: var(--ink); letter-spacing: 1px; }
  .nav { top: 34px; right: 56px; display: flex; gap: 31px; font-family: "Roboto Condensed", sans-serif; font-size: 15px; color: var(--ink); }
  .nav a { color: inherit; text-decoration: none; }
  .nav a.active { color: var(--orange); }

  .headline { left: 0; width: 830px; top: 163px; text-align: center; font-family: "Bebas Neue", sans-serif; font-weight: 400; font-size: 33px; color: var(--green-dark); white-space: nowrap; }
  .tagline { left: 0; width: 830px; top: 207px; text-align: center; font-family: "Roboto Condensed", sans-serif; font-size: 17px; color: var(--orange); }
  .btn-hero { left: 332px; top: 254px; width: 166px; height: 43px; background: var(--orange); color: var(--white); font-family: "Open Sans", sans-serif; font-weight: 700; font-size: 14px; display: flex; align-items: center; justify-content: center; letter-spacing: 0.3px; }

  .why { left: 54px; top: 388px; width: 722px; height: 252px; background: var(--green); color: var(--white); font-size: 11px; }
  .why h2 { position: absolute; left: 0; width: 100%; top: 26px; text-align: center; font-family: "Roboto Condensed", sans-serif; font-weight: 400; font-size: 29px; }
  .why p { position: absolute; text-align: center; line-height: 17.5px; }
  .why .lead { left: 20px; width: 682px; top: 78px; white-space: nowrap; }
  .why .cert-lead { left: 80px; width: 562px; top: 136px; }
  .tick-item { position: absolute; display: flex; align-items: center; gap: 8px; white-space: nowrap; }
  .tick-item svg { width: 12px; height: 12px; flex: none; }

  .contact-title { left: 0; width: 806px; top: 664px; text-align: center; font-family: "Roboto Condensed", sans-serif; font-weight: 400; font-size: 30px; color: var(--green); }
  .contact-copy { left: 105px; width: 620px; text-align: center; font-size: 11px; line-height: 17.5px; color: var(--text); }
  .services .tick-item { color: var(--amber); font-size: 13px; }
  .services svg { width: 13px; height: 13px; }
  .btn-now { left: 324px; top: 906px; width: 158px; height: 32px; background: var(--green); color: var(--white); font-family: "Roboto Condensed", sans-serif; font-size: 18px; display: flex; align-items: center; justify-content: center; letter-spacing: 0.5px; }

  .footer { left: 0; top: 984px; width: 830px; height: 216px; background: var(--orange); color: var(--white); }
  .footer h3 { position: absolute; top: 17px; font-family: "Roboto Condensed", sans-serif; font-weight: 400; font-size: 23px; }
  .links a { position: absolute; left: 55px; font-size: 12px; color: var(--white); text-decoration: none; }
  .links a.current { color: #1c1c1c; }
  .news-text { left: 308px; top: 54px; width: 200px; font-size: 11px; line-height: 17.5px; }
  .email-field { left: 307px; top: 98px; width: 216px; height: 25px; border: 1px solid var(--white); font-size: 11px; padding: 4px 6px; }
  .btn-sub { left: 307px; top: 134px; width: 108px; height: 25px; background: var(--white); color: var(--orange); font-family: "Roboto Condensed", sans-serif; font-size: 15px; display: flex; align-items: center; justify-content: center; }
  .reach { left: 577px; display: flex; gap: 10px; font-size: 10.5px; line-height: 14.5px; }
  .reach svg { width: 14px; height: 14px; flex: none; margin-top: 1px; }
  .social { left: 578px; top: 156px; display: flex; gap: 22px; font-size: 11px; font-weight: 600; }
  .rule { left: 54px; top: 181px; width: 722px; height: 1px; background: rgba(255,255,255,0.45); }
  .copyright { left: 0; width: 830px; top: 190px; text-align: center; font-size: 11.5px; }
  .copyright b { text-decoration: underline; }
</style>
</head>
<body>
<svg width="0" height="0" style="position:absolute">
  <defs>
    <symbol id="tick" viewBox="0 0 14 14">
      <path d="M11 7.5V12H2V3h7" fill="none" stroke="currentColor" stroke-width="1.6"/>
      <path d="M4.2 6.5l2.5 2.5L13 2.5" fill="none" stroke="currentColor" stroke-width="1.8"/>
    </symbol>
  </defs>
</svg>

<div class="abs hero" role="img" aria-label="Photo of hands using a calculator and pen over financial papers, faded light blue-grey"></div>

<div class="abs brand">VELTRO</div>
<nav class="abs nav">
  <a class="active" href="#">HOME</a>
  <a href="#">ABOUT</a>
  <a href="#">ADVISORY SERVICES</a>
  <a href="#">CONTACT US</a>
</nav>

<h1 class="abs headline">Over 35 years experience in audit and advisory services.</h1>
<p class="abs tagline">When you are ready to take that next step, we are there to keeep you on the right path.</p>
<div class="abs btn-hero">CONTACT US</div>

<section class="abs why">
  <h2>Why Veltro ?</h2>
  <p class="lead">Our proven implementation and audit models allow for capturing requirements while expiditing the process.</p>
  <div class="tick-item" style="left:40px;top:106px"><svg><use href="#tick"/></svg>Free consultation</div>
  <div class="tick-item" style="left:292px;top:106px"><svg><use href="#tick"/></svg>Fixed cost</div>
  <div class="tick-item" style="left:547px;top:106px"><svg><use href="#tick"/></svg>Results driven</div>
  <p class="cert-lead">Our professionals maintain certifications required for your service needs.&nbsp; We utilize the best so you get the best results.</p>
  <div class="tick-item" style="left:40px;top:181px"><svg><use href="#tick"/></svg>CPA</div>
  <div class="tick-item" style="left:292px;top:181px"><svg><use href="#tick"/></svg>CHP</div>
  <div class="tick-item" style="left:547px;top:181px"><svg><use href="#tick"/></svg>CISA</div>
  <div class="tick-item" style="left:40px;top:199px"><svg><use href="#tick"/></svg>CISSP</div>
  <div class="tick-item" style="left:292px;top:199px"><svg><use href="#tick"/></svg>ISO/IEC 27001</div>
</section>

<h2 class="abs contact-title">Contact Us Today!</h2>
<p class="abs contact-copy" style="top:718px">Whether you are fact finding or ready to make a decsion, we are happy to answer any questions you may have.&nbsp; Contact us today and find out why Veltro is the right fit for you.</p>
<p class="abs contact-copy" style="top:770px">We are happy to provide you with information on the following services:</p>
<div class="services">
  <div class="abs tick-item" style="left:162px;top:807px"><svg><use href="#tick"/></svg>SOC 1</div>
  <div class="abs tick-item" style="left:162px;top:832px"><svg><use href="#tick"/></svg>SOC 2</div>
  <div class="abs tick-item" style="left:162px;top:858px"><svg><use href="#tick"/></svg>CFPB Professional Services</div>
  <div class="abs tick-item" style="left:443px;top:807px"><svg><use href="#tick"/></svg>ISO 27002 Professional Services</div>
  <div class="abs tick-item" style="left:443px;top:832px"><svg><use href="#tick"/></svg>HIPAA Security Review</div>
  <div class="abs tick-item" style="left:443px;top:858px"><svg><use href="#tick"/></svg>IT Security Review</div>
</div>
<div class="abs btn-now">CONTACT US NOW</div>

<footer class="abs footer">
  <h3 style="left:55px">Useful Links</h3>
  <div class="links">
    <a class="current" href="#" style="top:59px">Home</a>
    <a href="#" style="top:88px">About</a>
    <a href="#" style="top:117px">Advisory Services</a>
    <a href="#" style="top:146px">Contact Us</a>
  </div>

  <h3 style="left:307px">Newsletter</h3>
  <p class="abs news-text">Sign up for short updates on audit standards and our latest news.</p>
  <div class="abs email-field">Enter Email Id</div>
  <div class="abs btn-sub">SUBSCRIBE</div>

  <h3 style="left:577px">Get In Touch With Us</h3>
  <div class="abs reach" style="top:55px">
    <svg viewBox="0 0 14 14"><path d="M7 13C4 9 3 7.3 3 5.5a4 4 0 0 1 8 0C11 7.3 10 9 7 13z" fill="currentColor"/><circle cx="7" cy="5.5" r="1.5" fill="var(--orange)"/></svg>
    <span>415 Harbor Lane, Suite 210,<br>Clearwater, FL 33755,<br>United States</span>
  </div>
  <div class="abs reach" style="top:107px">
    <svg viewBox="0 0 14 14"><path d="M3 1.5l2.5 0 1 3-1.5 1.2a7 7 0 0 0 3.3 3.3L9.5 7.5l3 1v2.5c0 .8-.7 1.5-1.5 1.5A10 10 0 0 1 1.5 3c0-.8.7-1.5 1.5-1.5z" fill="currentColor"/></svg>
    <span>+15550142290</span>
  </div>
  <div class="abs reach" style="top:132px">
    <svg viewBox="0 0 14 14"><rect x="1" y="3" width="12" height="8.5" rx="1" fill="currentColor"/><path d="M1.5 3.8L7 8l5.5-4.2" fill="none" stroke="var(--orange)" stroke-width="1.2"/></svg>
    <span>hello@veltrocheck.com</span>
  </div>
  <div class="abs social"><span>Circlet</span><span>Chirper</span><span>Linkup</span></div>

  <div class="abs rule"></div>
  <p class="abs copyright">© <b>VELTRO</b> - 2016. All Rights Reserved.</p>
</footer>
</body>
</html>
```